Non Profit Company Looking For New Website

The website for Corvale Paddock Rehoming Society should offer the viewer beautiful photos that inspire condifence and joy and tap into our love of horses.

We would like to see a website that displays trust, quality and confidence. Needs to be responsive and mobile friendly for all browsers and coded for both Android & IOS.

READ ATTACHED WEBSITE TEMPLATE FOR COMPLETE DETAILS ON WHAT WE ARE LOOKING FOR.

Looking for recommmendations if we should use WordPress/WooCommerce for site or Wordpress with Shopify Plug in or just Shopify.

Must be both desktop and mobile friendly with fast page load speed. Need the ability to edit ourselves.

Industry/Entity Type

Non Profit

Coding

Coded - Design and coding required

Number of Pages Required

5+ page

Requirements
Must have
• We would like to see a website that displays trust, quality and confidence. Needs to be responsive and mobile friendly for all browsers and coded for both Android & IOS.

Looking for recommendations if we should use WordPress/WooCommerce for site or Wordpress with Shopify Plug in or just Shopify.

Logo Colour:
Pantone 7621 C

READ TEMPLATE THAT IS ATTACHED
Nice to have
• Like look of this website as a sample:
https://www.quillmanegallop.com/

Another similar non profit organization
https://brindlefieldrest.com/

```html
<!DOCTYPE html>
<html lang="en">
<head>
<meta charset="utf-8">
<title>Corvale Paddock Rehoming Society</title>
<link href="https://fonts.googleapis.com/css2?family=Cinzel:wght@400;600;700&family=Montserrat:wght@400;500;600;700&display=swap" rel="stylesheet">
<style>
:root{
  --red:#b3202f;
  --red-dark:#8e1622;
  --red-soft:#d9525e;
  --ink:#2b2b2b;
  --muted:#666;
  --grey-bg:#f1f1f3;
  --black:#0d0d0d;
  --white:#fff;
}
*{box-sizing:border-box;margin:0;padding:0}
html,body{width:1200px;height:3628px;overflow:hidden}
body{position:relative;background:var(--white);font-family:'Montserrat',sans-serif;color:var(--ink)}
.abs{position:absolute}
h2,h3{font-family:'Cinzel',serif;color:var(--red);font-weight:600}
.btn{display:inline-block;background:var(--red);color:#fff;font-size:12px;font-weight:700;letter-spacing:1px;text-transform:uppercase;padding:12px 24px;border-radius:3px}

/* header */
.logo{left:40px;top:12px;display:flex;gap:10px;align-items:center;color:var(--red);font-weight:700;font-size:16px;line-height:1.15;text-transform:uppercase}
.logo .mark{width:30px;height:30px;border-radius:50%;background:var(--red);flex:none}
.logo small{display:block;font-size:9px;letter-spacing:1px;margin-top:3px}
.call{right:170px;top:12px;display:flex;align-items:center;gap:10px;font-size:13px;color:var(--ink)}
.call .ic{width:32px;height:32px;border-radius:50%;border:2px solid var(--red);display:flex;align-items:center;justify-content:center}
.call b{display:block;font-size:11px;color:var(--red)}
.top-social{right:40px;top:18px;display:flex;gap:6px}
.dot{width:22px;height:22px;border-radius:50%;border:1.5px solid var(--ink)}
.nav{left:340px;top:62px;width:860px;height:40px;background:var(--red);border-radius:20px 0 0 20px;display:flex;align-items:center;justify-content:space-around;padding:0 40px}
.nav a{color:#fff;text-decoration:none;font-size:13px;font-weight:600;letter-spacing:1px;text-transform:uppercase}
.nav a.on{border-bottom:2px solid #fff;padding-bottom:3px}

/* hero */
.hero{left:0;top:112px;width:1200px;height:690px;background:
  radial-gradient(ellipse 30% 45% at 78% 30%,rgba(240,230,190,.55),rgba(0,0,0,0) 70%),
  radial-gradient(ellipse 18% 40% at 22% 55%,rgba(205,130,140,.45),rgba(0,0,0,0) 70%),
  radial-gradient(ellipse at 50% 40%,#7c8f55 0%,#3f5a2c 50%,#1f2f18 100%)}
.hero h1{position:absolute;left:0;right:0;top:430px;text-align:center;font-family:'Cinzel',serif;color:#fff;font-weight:600;font-size:32px;line-height:1.3;letter-spacing:1px;text-shadow:0 2px 6px rgba(0,0,0,.5)}
.hero-curve{left:0;top:700px;width:1200px;height:130px}

/* pillars */
.pillars{left:0;top:790px;width:1200px;display:flex;justify-content:center;gap:72px}
.pillar{width:150px;height:150px;border-radius:50%;background:radial-gradient(circle,#fff 55%,#e6e6e8);box-shadow:0 6px 16px rgba(0,0,0,.18);display:flex;align-items:center;justify-content:center}
.pillar span{width:74px;height:74px;border-radius:50%;background:radial-gradient(circle at 45% 40%,var(--red-soft),var(--red) 60%,var(--red-dark))}
.tagline{left:0;top:1010px;width:1200px;text-align:center;font-size:30px;letter-spacing:2px}
.intro{left:0;top:1064px;width:1200px;text-align:center;font-size:15px;line-height:1.7}

/* what is */
.what-photo{left:60px;top:1160px;width:460px;height:400px;background:
  radial-gradient(ellipse 25% 50% at 28% 58%,#5a3d29,rgba(90,61,41,0) 75%),
  radial-gradient(ellipse 22% 45% at 62% 55%,#ece6de,rgba(236,230,222,0) 75%),
  radial-gradient(ellipse at 20% 20%,#f8e8ea,#fff 70%)}
.what{left:555px;top:1200px;width:520px}
.what h2{font-size:38px;line-height:1.15;letter-spacing:1px;margin-bottom:22px}
.what p{font-size:12.5px;line-height:1.75;color:var(--muted);margin-bottom:14px}

/* adopt */
.adopt-bg{left:0;top:1600px;width:1200px;height:900px;background:var(--grey-bg)}
.adopt-head{left:0;top:1650px;width:1200px;text-align:center}
.adopt-head h2{font-size:40px;letter-spacing:1px}
.adopt-head p{font-size:14px;margin:12px 0 20px}
.grid{left:160px;top:1892px;width:880px;display:grid;grid-template-columns:repeat(3,280px);gap:28px 20px}
.tile{height:220px;border-radius:6px}
.t1{background:linear-gradient(160deg,#cfd5c0 0%,#9a5a32 45%,#5c3118 75%,#e8e4dc 100%)}
.t2{background:linear-gradient(180deg,#3b2d22 0%,#6b4a2e 45%,#b59a74 75%,#d8c6a4 100%)}
.t3{background:linear-gradient(180deg,#b9c48c 0%,#e9e7e2 45%,#6a4a32 70%,#8aa05a 100%)}
.t4{background:linear-gradient(180deg,#2f4a22 0%,#4f6f35 45%,#e5e3dc 70%,#6f8d45 100%)}
.t5{background:linear-gradient(180deg,#f2f1ec 0%,#5b5f3a 30%,#2a2420 60%,#3e4a2a 100%)}
.t6{background:linear-gradient(180deg,#f1f3f6 0%,#d8e4ef 35%,#6b3f22 60%,#e2cf48 100%)}
.more{left:0;top:2390px;width:1200px;text-align:center}

/* difference */
.diff{left:160px;top:2500px;width:400px}
.diff h2{font-size:36px;letter-spacing:1px;margin-bottom:18px}
.diff p{font-size:13px;line-height:1.7;color:var(--muted);margin-bottom:16px}
.diff-photo{left:592px;top:2520px;width:448px;height:400px;border-radius:6px;background:
  radial-gradient(ellipse 35% 45% at 40% 45%,#e6e4df,rgba(230,228,223,0) 75%),
  radial-gradient(ellipse 25% 45% at 75% 70%,#2f3640,rgba(47,54,64,0) 80%),
  linear-gradient(135deg,#c9b48a,#7d6a4c 55%,#3a342c)}

/* footer & contact */
.footer{left:0;top:3330px;width:1200px;height:298px;background:var(--black)}
.contact{left:148px;top:3000px;width:904px;height:400px;display:flex;box-shadow:0 10px 28px rgba(0,0,0,.2)}
.form{width:524px;background:#fff;padding:36px 48px}
.form h2{text-align:center;font-size:36px;letter-spacing:1px}
.form .sub{text-align:center;font-size:11px;color:var(--muted);margin:6px 0 20px}
.row{display:flex;gap:14px;margin-bottom:12px}
.field{flex:1;height:38px;border:1px solid #ddd;border-radius:3px;font-size:11px;color:#999;padding:11px 12px}
.field.msg{height:86px}
.form-foot{display:flex;justify-content:space-between;align-items:center;margin-top:4px}
.captcha{width:220px;height:56px;border:1px solid #ccc;border-radius:3px;background:#f9f9f9;display:flex;align-items:center;gap:10px;padding:0 12px;font-size:12px}
.captcha i{width:20px;height:20px;border:2px solid #bbb;background:#fff;display:block}
.details{width:380px;background:var(--red);color:#fff;padding:40px 36px}
.details h2{color:#fff;font-size:26px;letter-spacing:1px;margin-bottom:30px;white-space:nowrap}
.item{display:flex;gap:14px;margin-bottom:24px}
.item .ic{width:30px;height:30px;flex:none}
.item b{display:block;font-size:13px;letter-spacing:1px;margin-bottom:4px}
.item span{font-size:13px;line-height:1.5}
.fnav{left:0;top:3476px;width:1200px;display:flex;justify-content:center;gap:96px}
.fnav a{color:#fff;text-decoration:none;font-size:13px;letter-spacing:1px;text-transform:uppercase}
.fline{left:160px;top:3540px;width:880px;height:1px;background:#333}
.copy{left:160px;top:3570px;font-size:12px;color:#ccc}
.fsocial{right:160px;top:3562px;display:flex;gap:8px}
.fsocial .dot{border-color:#fff;width:26px;height:26px}
</style>
</head>
<body>

<header>
  <div class="abs logo"><span class="mark"></span><span>Corvale<br>Paddock<small>Rehoming Society</small></span></div>
  <div class="abs call">
    <span class="ic"><svg width="16" height="16" viewBox="0 0 24 24"><path fill="#b3202f" d="M6.6 10.8a15 15 0 0 0 6.6 6.6l2.2-2.2c.3-.3.7-.4 1-.2 1.1.4 2.3.6 3.6.6.6 0 1 .4 1 1V20c0 .6-.4 1-1 1A17 17 0 0 1 3 4c0-.6.4-1 1-1h3.5c.6 0 1 .4 1 1 0 1.3.2 2.5.6 3.6.1.3 0 .7-.2 1z"/></svg></span>
    <span><b>CALL US</b>(555) 014-2298</span>
  </div>
  <div class="abs top-social"><span class="dot"></span><span class="dot"></span><span class="dot"></span><span class="dot"></span></div>
  <nav class="abs nav">
    <a class="on">Home</a><a>About</a><a>Adopt</a><a>Horses</a><a>Donate/Shop</a><a>Contact</a>
  </nav>
</header>

<section class="abs hero" role="img" aria-label="Woman in a pink dress standing with a chestnut horse in a sunlit forest">
  <h1>We Support And Develop Retired Thoroughbred<br>Racehorses For Their Next Chapter In Life</h1>
</section>
<svg class="abs hero-curve" viewBox="0 0 1200 130" preserveAspectRatio="none">
  <path d="M0 30 Q600 140 1200 30 L1200 130 L0 130Z" fill="#fff"/>
  <path d="M0 10 Q600 130 1200 10 L1200 30 Q600 150 0 30Z" fill="#b3202f"/>
</svg>

<section>
  <div class="abs pillars">
    <div class="pillar" role="img" aria-label="Red horse icon for retire"><span></span></div>
    <div class="pillar" role="img" aria-label="Red harness racing icon for retrain"><span></span></div>
    <div class="pillar" role="img" aria-label="Red rider icon for rehome"><span></span></div>
  </div>
  <h3 class="abs tagline">Retire, Retrain, Rehome</h3>
  <p class="abs intro">Corvale Paddock Rehoming Society (CPRS) is a registered not-for-profit<br>organization in Alberta.</p>
</section>

<section>
  <div class="abs what-photo" role="img" aria-label="Rider in a helmet hugging her bay horse"></div>
  <div class="abs what">
    <h2>What Is Thoroughbred<br>Aftercare?</h2>
    <p>The health, safety and welfare of our equine athletes does not end at the finish line, and retirement and aftercare are critical to the success of the racing industry.</p>
    <p>Aftercare is the safe placement of racehorses after their careers as racehorses are completed. Some horses might retire to the breeding shed or broodmare bands, while others are retrained for second careers.</p>
    <span class="btn" style="margin-top:6px">Learn more about us</span>
  </div>
</section>

<section>
  <div class="abs adopt-bg"></div>
  <div class="abs adopt-head">
    <h2>Adopt A Horse</h2>
    <p>Corvale Paddock Rehoming is committed to helping match you with the perfect horse.</p>
    <span class="btn">Adopt now</span>
  </div>
  <div class="abs grid">
    <div class="tile t1" role="img" aria-label="Chestnut horse looking over a white fence"></div>
    <div class="tile t2" role="img" aria-label="Bay horse standing in a sandy arena"></div>
    <div class="tile t3" role="img" aria-label="Grey and bay horses grazing together"></div>
    <div class="tile t4" role="img" aria-label="White horse in a green meadow"></div>
    <div class="tile t5" role="img" aria-label="Dark horse portrait with bridle"></div>
    <div class="tile t6" role="img" aria-label="Brown horse in a field of yellow flowers"></div>
  </div>
  <div class="abs more"><span class="btn">More ways to give</span></div>
</section>

<section>
  <div class="abs diff">
    <h2>Make A Difference</h2>
    <p>Every gift helps a retired racehorse find safe pasture, patient training and a loving home. Your support funds feed, farrier care and vet visits.</p>
    <p>Our volunteers give their time to groom, ride and assess each horse, so adopters can meet a partner that truly suits them. Join us and help write the next chapter.</p>
    <span class="btn">Donate</span>
  </div>
  <div class="abs diff-photo" role="img" aria-label="Man gently touching a grey horse's neck at sunset"></div>
</section>

<footer>
  <div class="abs footer"></div>
  <div class="abs contact">
    <div class="form">
      <h2>Get In Touch</h2>
      <p class="sub">Send us a note and our team will reply within two working days.</p>
      <div class="row"><div class="field">First Name</div><div class="field">Last Name</div></div>
      <div class="row"><div class="field">Email</div><div class="field">Phone No.</div></div>
      <div class="row"><div class="field msg">Message</div></div>
      <div class="form-foot">
        <div class="captcha"><i></i>I'm not a robot</div>
        <span class="btn">Submit</span>
      </div>
    </div>
    <div class="details">
      <h2>Contact Details</h2>
      <div class="item">
        <svg class="ic" viewBox="0 0 24 24"><path fill="#fff" d="M12 2a7 7 0 0 0-7 7c0 5 7 13 7 13s7-8 7-13a7 7 0 0 0-7-7zm0 9.5A2.5 2.5 0 1 1 12 6.5a2.5 2.5 0 0 1 0 5z"/></svg>
        <div><b>LOCATION</b><span>48 Tallow Ridge Road,<br>Fernmoor, AB T0C 2K0</span></div>
      </div>
      <div class="item">
        <svg class="ic" viewBox="0 0 24 24"><path fill="#fff" d="M6.6 10.8a15 15 0 0 0 6.6 6.6l2.2-2.2c.3-.3.7-.4 1-.2 1.1.4 2.3.6 3.6.6.6 0 1 .4 1 1V20c0 .6-.4 1-1 1A17 17 0 0 1 3 4c0-.6.4-1 1-1h3.5c.6 0 1 .4 1 1 0 1.3.2 2.5.6 3.6.1.3 0 .7-.2 1z"/></svg>
        <div><b>CALL US</b><span>(555) 014-2298</span></div>
      </div>
      <div class="item">
        <svg class="ic" viewBox="0 0 24 24"><path fill="#fff" d="M3 5h18v14H3zm2 2v.5l7 4.5 7-4.5V7l-7 4.5z"/></svg>
        <div><b>EMAIL US</b><span>hello@corvalepaddock.org</span></div>
      </div>
    </div>
  </div>
  <nav class="abs fnav"><a>Home</a><a>About</a><a>Adopt</a><a>Horses</a><a>Donate/Shop</a><a>Contact</a></nav>
  <div class="abs fline"></div>
  <p class="abs copy">Copyright © 2024. Corvale Paddock Rehoming Society. All Rights Reserved</p>
  <div class="abs fsocial"><span class="dot"></span><span class="dot"></span><span class="dot"></span><span class="dot"></span></div>
</footer>

</body>
</html>
```